Business Card Design - Property Management & Real Estate Services

I need a business card design for my company that I can print ZEP Cards. The company is called Brisk Management Company. It is a property management and real estate company. The design has to be clean and modern. I need two versions. One for my employee and one for me. However, the design will be the same, just different text. You can get a feel for the company by looking at our website at www.briskmanagement.example.

Industry/Entity Type

Property Management

Contact Information for Business Card

I will be using ZEP.com to print my cards. I will most likely use the rounded edges card. I need two versions, however, they will be the same design. I need one for me and my employee.

Colors
3276b5
33a6d7

Requirements
Must have
• Company Logo
• Name of person
• Property Management & Real Estate Service
• Phone
• Email
• Website
• Address
• A space to place a QR code

```html
<!DOCTYPE html>
<html lang="en">
<head>
<meta charset="UTF-8">
<title>Brisk Management – Business Card</title>
<link rel="stylesheet" href="https://fonts.googleapis.com/css2?family=Montserrat:wght@400;500;600&display=swap">
<style>
  :root {
    --page-bg: #d9d9db;
    --card-white: #ffffff;
    --card-blue: #70a0d1;
    --brand-dark: #1f4fa6;
    --brand-light: #5b8fd8;
    --text-grey: #4a4a4a;
    --back-mark: #e6f0fb;
  }
  * { box-sizing: border-box; margin: 0; padding: 0; }
  html, body {
    width: 1200px; height: 800px; overflow: hidden;
    background: var(--page-bg);
    font-family: "Montserrat", Arial, sans-serif;
  }
  .sheet {
    width: 1200px; height: 800px;
    display: flex; align-items: center; justify-content: center; gap: 50px;
  }
  .card {
    width: 525px; height: 300px;
    border-radius: 24px;
    position: relative;
    box-shadow: 0 6px 18px rgba(0,0,0,0.12);
  }
  .card--front { background: var(--card-white); display: flex; align-items: center; }
  .card--back { background: var(--card-blue); display: flex; align-items: center; justify-content: center; }

  .brand-name {
    font-weight: 500;
    color: var(--brand-dark);
    text-transform: uppercase;
    text-align: center;
    line-height: 1.15;
  }
  .front-brand {
    width: 240px; padding-left: 30px;
    font-size: 30px; letter-spacing: 2px;
  }
  .front-brand .brand-sub { display: block; font-size: 30px; }

  .divider {
    width: 1px; height: 130px; background: var(--brand-dark);
    margin: 0 26px 0 14px;
  }

  .details { flex: 1; padding-right: 20px; }
  .person-name {
    font-size: 22px; font-weight: 500; color: var(--brand-dark);
    text-transform: uppercase; letter-spacing: 0.5px;
  }
  .person-role {
    font-size: 14px; color: var(--brand-light); line-height: 1.3; margin-top: 3px;
  }
  .address {
    font-size: 13.5px; color: var(--text-grey); line-height: 1.35; margin-top: 18px;
  }
  .contact-list { list-style: none; margin-top: 14px; }
  .contact-list li {
    display: flex; align-items: center; gap: 8px;
    font-size: 13px; color: var(--text-grey); line-height: 1.5;
  }
  .contact-icon { width: 11px; height: 11px; flex-shrink: 0; }

  .back-brand {
    color: var(--back-mark);
    font-size: 46px; letter-spacing: 4px;
  }
</style>
</head>
<body>
<main class="sheet">
  <section class="card card--front" aria-label="Card front">
    <div class="brand-name front-brand">Brisk<span class="brand-sub">Management</span></div>
    <div class="divider"></div>
    <div class="details">
      <h1 class="person-name">Daniel Brooks</h1>
      <p class="person-role">Property Management<br>Real Estate Service</p>
      <p class="address">480 Harbor Ave #210<br>Coral Bay, FL 33000</p>
      <ul class="contact-list">
        <li>
          <svg class="contact-icon" viewBox="0 0 12 12"><path fill="var(--brand-dark)" d="M2.5 0.8 4.3 2.9 3.4 4.1c.7 1.5 1.8 2.6 3.3 3.4l1.1-.9L10 8.5 9 10.6C5 10.4 1.5 7 1.3 2.9Z"/></svg>
          (555) 201-4836
        </li>
        <li>
          <svg class="contact-icon" viewBox="0 0 12 12"><rect x="0.5" y="2" width="11" height="8" rx="1" fill="var(--brand-dark)"/><path d="M1 2.6 6 6.6 11 2.6" fill="none" stroke="#fff" stroke-width="1"/></svg>
          info@briskmanagement.example
        </li>
        <li>
          <svg class="contact-icon" viewBox="0 0 12 12"><circle cx="6" cy="6" r="5.5" fill="var(--brand-dark)"/><path d="M0.8 6H11.2M6 0.8C3.8 3.5 3.8 8.5 6 11.2M6 0.8C8.2 3.5 8.2 8.5 6 11.2" fill="none" stroke="#fff" stroke-width="0.8"/></svg>
          www.briskmanagement.example
        </li>
      </ul>
    </div>
  </section>

  <section class="card card--back" aria-label="Card back">
    <div class="brand-name back-brand">Brisk<br>Management</div>
  </section>
</main>
</body>
</html>
```